White Cane Law Awareness Poster

Open Harbor is a disability advocacy organization in Indiana. We are working on a project with the Tallmere Union of Low-Sight Tradespeople. Our organizations need a design for a poster to promote awareness of Indiana's White Cane law. This poster will be displayed in local libraries, businesses, and other public places.

The poster should catch people's attention, and briefly explain that drivers have to yield for pedestrians who are blind who have white canes or seeing eye dogs.

The poster should be designed with people with low vision in mind. This means large text in a clear font, with good contrast between the text and the background. The text should be in a sans serif font that is clear and easy to read, with no italics or script fonts. There should not be a "busy" picture or pattern behind the text.

The poster should also include a reference to the relevant laws. We have attached a document with those references.

Finally, the poster should include the logos of Open Harbor and the Tallmere Union of Low-Sight Tradespeople, which we have included as attachments.

We have also included an attachment with a photo of the old White Cane Law poster, just to show an example of what we DO NOT want.

Industry/Entity Type

Non-Profit

Font styles to use
Sans Serif

Requirements
Must have
• The poster should also include a reference to the relevant laws. We have attached a document with those references.
• Finally, the poster should include the logos of Open Harbor and the Tallmere Union of Low-Sight Tradespeople, which we have included as attachments.

```html
<!DOCTYPE html>
<html lang="en">
<head>
<meta charset="utf-8">
<title>White Cane Law Awareness Poster</title>
<link rel="stylesheet" href="https://fonts.googleapis.com/css2?family=Arimo:wght@400;700&display=swap">
<style>
  :root {
    --ink: #111111;
    --alert-red: #e8202a;
    --partner-blue: #1f3fd8;
    --paper: #ffffff;
    --swirl-light: #ececec;
    --swirl-mid: #d2d2d2;
  }
  html, body {
    margin: 0;
    padding: 0;
    overflow: hidden;
    background: var(--paper);
  }
  .poster {
    position: relative;
    width: 800px;
    height: 1200px;
    overflow: hidden;
    background: var(--paper);
    font-family: "Arimo", Arial, sans-serif;
    color: var(--ink);
  }
  .backdrop {
    position: absolute;
    inset: 0;
    background:
      linear-gradient(160deg, var(--swirl-mid) 0%, var(--swirl-light) 18%, var(--paper) 34%, var(--paper) 66%, var(--swirl-light) 84%, var(--swirl-mid) 100%);
  }
  .partner {
    position: absolute;
    display: flex;
    align-items: center;
    gap: 10px;
    font-weight: 700;
  }
  .partner--union {
    left: 18px;
    top: 40px;
    width: 250px;
    font-size: 19px;
    line-height: 1.2;
    color: var(--ink);
  }
  .partner--union .partner-dot {
    flex: 0 0 auto;
    width: 34px;
    height: 34px;
    border-radius: 50%;
    background: var(--ink);
  }
  .partner--harbor {
    right: 18px;
    top: 115px;
    font-size: 36px;
    color: var(--partner-blue);
  }
  .partner--harbor .partner-dot {
    width: 22px;
    height: 22px;
    background: var(--partner-blue);
  }
  .alert-ring {
    position: absolute;
    left: 30px;
    top: 178px;
  }
  .warning-icon {
    position: absolute;
    left: 351px;
    top: 240px;
  }
  .headline {
    position: absolute;
    left: 150px;
    top: 356px;
    width: 500px;
    margin: 0;
    text-align: center;
    font-size: 35px;
    line-height: 45.8px;
    font-weight: 700;
  }
  .law-reference {
    position: absolute;
    left: 6px;
    top: 938px;
    width: 790px;
    font-size: 17px;
    line-height: 24.5px;
  }
  .law-reference h2 {
    margin: 0;
    font-size: 22px;
    line-height: 28px;
    font-weight: 700;
  }
  .law-reference p {
    margin: 0;
  }
  .law-reference .penalty {
    margin-top: 10px;
  }
</style>
</head>
<body>
<main class="poster">
  <div class="backdrop" role="img" aria-label="Soft grey flowing wave background"></div>

  <div class="partner partner--union">
    <span class="partner-dot"></span>
    <span>Tallmere Union of Low-Sight Tradespeople</span>
  </div>

  <div class="partner partner--harbor">
    <span class="partner-dot"></span>
    <span>Open Harbor</span>
  </div>

  <svg class="alert-ring" width="740" height="730" viewBox="0 0 740 730" aria-hidden="true">
    <ellipse cx="370" cy="365" rx="342" ry="340" fill="var(--paper)" stroke="var(--alert-red)" stroke-width="30"/>
  </svg>

  <svg class="warning-icon" width="118" height="104" viewBox="0 0 118 104" aria-hidden="true">
    <path d="M59 8 L111 98 H7 Z" fill="none" stroke="var(--ink)" stroke-width="9" stroke-linejoin="round"/>
    <rect x="54" y="36" width="10" height="34" rx="4" fill="var(--ink)"/>
    <circle cx="59" cy="82" r="6" fill="var(--ink)"/>
  </svg>

  <h1 class="headline">Indiana Law<br>requires<br>drivers to come to a<br>complete stop<br>when encountering a<br>pedestrian<br>crossing a street<br>and guided by a dog<br>or carrying a<br>white cane</h1>

  <section class="law-reference">
    <h2>Indiana White Cane Law</h2>
    <p>Ind. Code § 9-21-17-21 : Indiana Code - Section 9-21-17-21: Blind pedestrians;<br>yield of right-of-way</p>
    <p>A person who drives a vehicle shall yield the right-of-way to a blind pedestrian carrying a clearly visible white cane or accompanied by a guide dog.</p>
    <h2 class="penalty">Penalty</h2>
    <p>Ind. Code § 9-21-17-24 : Indiana Code - Section 9-21-17-24: Violations;<br>Class C infraction</p>
    <p>A person who violates this chapter commits a Class C infraction. (Misdemeanor)</p>
  </section>
</main>
</body>
</html>
```